Benefits of Supplement Infographic - character illustration of health benefits

we are a supplement company who want to have an infographic that shows the benefits of the supplement, We have a few key areas which we have sketched out and have also included an excel spreadsheet with some detail that relates to the visual attached. Obviously these are very high level concepts, please reach out to me with any questions.

Target Market(s)

Our customers will be affluent millennials and adults who are health conscious also frontline workers e.g. police, firemen, doctors, nurses who want to boost immunity.

Font styles to use
Sans Serif

Colors
3176b5
876aae
9bcb3c

Requirements
Must have
• General: Characters need to be illustrations, match stick men would be ideal. Want it to be playful.
Athletes: 2 people running.
Lifestyle Stress: Person sitting at desk on laptop, lightening emblems at head to represent stress.
Physical stress: Firefighter character needed as study was on firefighter population.
Children: Children playing, skipping rope ideal.
Elderly: 2 characters on bikes will suffice here.

```html
<!DOCTYPE html>
<html lang="en">
<head>
<meta charset="utf-8">
<title>Supplement Benefits Infographic</title>
<link href="https://fonts.googleapis.com/css2?family=Fira+Sans+Condensed:wght@500;600;700&display=swap" rel="stylesheet">
<style>
  :root {
    --purple: #6e3f94;
    --green: #7dbf3f;
    --frame-green: #8cc63f;
    --lawn: #6cb33f;
    --shadow-purple: #5a2f7c;
    --ink: #2a2a2a;
    --bg: #ffffff;
  }
  html, body {
    margin: 0;
    width: 1200px;
    height: 644px;
    overflow: hidden;
    background: var(--bg);
  }
  .infographic {
    display: block;
    width: 1200px;
    height: 644px;
    font-family: "Fira Sans Condensed", "Arial Narrow", sans-serif;
  }
  .connector { fill: none; stroke: var(--purple); stroke-width: 1.3; }
  .connector-end { fill: var(--bg); stroke: var(--purple); stroke-width: 1.3; }
  .card-frame { fill: none; stroke: var(--frame-green); stroke-width: 1.6; }
  .ground-lawn { fill: var(--lawn); }
  .ground-shadow { fill: var(--shadow-purple); }
  .category { fill: var(--purple); font-weight: 700; font-size: 19px; text-anchor: middle; letter-spacing: 0.2px; }
  .stat { fill: var(--green); font-weight: 700; font-size: 23px; }
  .stat-big { font-size: 30px; }
  .stat-note { fill: var(--ink); font-weight: 600; font-size: 5.4px; }
  .stat-note-lg { font-size: 7px; }
</style>
</head>
<body>
<svg class="infographic" viewBox="0 0 850 456" xmlns="http://www.w3.org/2000/svg">
  <defs>
    <linearGradient id="tone-athletes" x1="0" y1="0" x2="0" y2="1">
      <stop offset="0" stop-color="#3aa9c9" stop-opacity="0.55"/>
      <stop offset="0.55" stop-color="#2f5d9a" stop-opacity="0.5"/>
      <stop offset="1" stop-color="#f0b48a" stop-opacity="0.45"/>
    </linearGradient>
    <linearGradient id="tone-lifestyle" x1="0" y1="0" x2="1" y2="1">
      <stop offset="0" stop-color="#f7c48a" stop-opacity="0.7"/>
      <stop offset="0.6" stop-color="#f39a2c" stop-opacity="0.6"/>
      <stop offset="1" stop-color="#8a8fa3" stop-opacity="0.55"/>
    </linearGradient>
    <linearGradient id="tone-physical" x1="0" y1="0" x2="0" y2="1">
      <stop offset="0" stop-color="#b9bcc6" stop-opacity="0.55"/>
      <stop offset="0.5" stop-color="#3b4660" stop-opacity="0.6"/>
      <stop offset="1" stop-color="#2a3148" stop-opacity="0.7"/>
    </linearGradient>
    <linearGradient id="tone-children" x1="0" y1="0" x2="1" y2="1">
      <stop offset="0" stop-color="#f9d35a" stop-opacity="0.6"/>
      <stop offset="0.45" stop-color="#d97bc7" stop-opacity="0.55"/>
      <stop offset="1" stop-color="#f26b3a" stop-opacity="0.55"/>
    </linearGradient>
    <linearGradient id="tone-elder" x1="0" y1="0" x2="0" y2="1">
      <stop offset="0" stop-color="#d8d4cf" stop-opacity="0.6"/>
      <stop offset="0.45" stop-color="#c8473b" stop-opacity="0.55"/>
      <stop offset="1" stop-color="#6f7c8c" stop-opacity="0.6"/>
    </linearGradient>
  </defs>

  <!-- connecting timeline -->
  <path class="connector" d="M72,222 V95 H212 V386 H350 V44 H490 V386 H630 V95 H770 V217"/>
  <circle class="connector-end" cx="72" cy="222" r="4"/>
  <circle class="connector-end" cx="770" cy="217" r="4"/>

  <!-- Athletes -->
  <g class="benefit benefit--athletes">
    <rect class="card-frame" x="82" y="104" width="120" height="212"/>
    <g role="img" aria-label="Illustration of two athletes, one skipping rope and one lifting a barbell, on a green lawn">
      <ellipse class="ground-lawn" cx="142" cy="220" rx="47" ry="13"/>
      <rect x="106" y="118" width="84" height="108" rx="36" fill="url(#tone-athletes)"/>
    </g>
    <text class="category" x="142" y="276">ATHLETES</text>
    <text class="stat" x="94" y="301">40%</text>
    <text class="stat-note" x="160" y="291">Reduction in</text>
    <text class="stat-note" x="160" y="298">URTI Symptoms</text>
  </g>

  <!-- Lifestyle stress -->
  <g class="benefit benefit--lifestyle">
    <g role="img" aria-label="Illustration of a stressed young man sitting hugging his knees in front of a mirror">
      <ellipse class="ground-shadow" cx="276" cy="288" rx="50" ry="7"/>
      <rect x="238" y="195" width="88" height="92" rx="30" fill="url(#tone-lifestyle)"/>
    </g>
    <text class="category" x="281" y="319">LIFESTYLE</text>
    <text class="category" x="281" y="337">STRESS</text>
    <text class="stat" x="232" y="364">70%</text>
    <text class="stat-note" x="285" y="353">Reduction in</text>
    <text class="stat-note" x="285" y="360">URTI Days</text>
  </g>

  <!-- Physical stress -->
  <g class="benefit benefit--physical">
    <rect class="card-frame" x="360" y="54" width="120" height="226"/>
    <g role="img" aria-label="Illustration of a businessman running through flying papers, a briefcase and office items">
      <ellipse class="ground-shadow" cx="420" cy="181" rx="52" ry="10"/>
      <rect x="372" y="72" width="104" height="112" rx="40" fill="url(#tone-physical)"/>
    </g>
    <text class="category" x="420" y="219">PHYSICAL</text>
    <text class="category" x="420" y="236">STRESS</text>
    <text class="stat" x="370" y="262">40%</text>
    <text class="stat-note" x="422" y="251">Reduction in</text>
    <text class="stat-note" x="422" y="258">URTI Symptoms</text>
  </g>

  <!-- Children -->
  <g class="benefit benefit--children">
    <g role="img" aria-label="Illustration of two children jumping and playing on a green lawn">
      <ellipse class="ground-lawn" cx="563" cy="284" rx="47" ry="12"/>
      <rect x="510" y="188" width="106" height="90" rx="38" fill="url(#tone-children)"/>
    </g>
    <text class="category" x="563" y="329">CHILDREN</text>
    <text class="stat stat-big" x="536" y="363">6</text>
    <text class="stat-note stat-note-lg" x="558" y="348">Fewer</text>
    <text class="stat-note stat-note-lg" x="558" y="356">Sick Days</text>
  </g>

  <!-- Elder -->
  <g class="benefit benefit--elder">
    <rect class="card-frame" x="640" y="104" width="120" height="226"/>
    <g role="img" aria-label="Illustration of an elderly couple standing together, the man holding a cane">
      <rect x="656" y="133" width="90" height="126" rx="34" fill="url(#tone-elder)"/>
    </g>
    <text class="category" x="700" y="289">ELDER</text>
    <text class="stat" x="652" y="315">16%</text>
    <text class="stat-note" x="701" y="303">Reduction in</text>
    <text class="stat-note" x="701" y="310">URTI Symptoms</text>
  </g>
</svg>
</body>
</html>
```